Brightvale HQ letterhead and envelope

Design a formal (8.5x11) letterhead and envelope for sales outreach and legal matters. Using design input from https://www.brightvalehq.example/ and the attached documents.

Industry/Entity Type

Software Service

Requirements
Must have
• These 4 hex colors are our official colors:
• #355c98 [blue]
• #1eb1a2 [teal]
• #fdba12 [gold]
• #f1653b [orange]
• So no other colors besides these should be used.

```html
<!DOCTYPE html>
<html lang="en">
<head>
<meta charset="UTF-8">
<title>Brightvale HQ Letterhead</title>
<link href="https://fonts.googleapis.com/css2?family=Didact+Gothic&family=Arimo:wght@700&display=swap" rel="stylesheet">
<style>
  :root {
    --brand-blue: #355c98;
    --paper: #ffffff;
    --ink: #2e2e2e;
    --muted: #555555;
    --backdrop: #dfe6f3;
    --watermark: rgba(53, 92, 152, 0.07);
  }
  * { box-sizing: border-box; margin: 0; padding: 0; }
  html, body {
    width: 1200px; height: 893px; overflow: hidden;
    background: var(--backdrop);
    font-family: "Didact Gothic", sans-serif;
  }
  .letterhead {
    position: absolute; left: 270px; top: 20px;
    width: 660px; height: 853px;
    background: var(--paper);
    box-shadow: 0 6px 24px rgba(53, 92, 152, 0.18);
    overflow: hidden;
  }
  .corner-block {
    position: absolute; left: 0; top: 118px;
    width: 70px; height: 72px;
    background: var(--brand-blue);
  }
  .brand {
    position: absolute; left: 86px; top: 128px;
    display: flex; align-items: center; gap: 12px;
  }
  .brand-dot {
    width: 36px; height: 36px; border-radius: 50%;
    border: 3px solid var(--brand-blue);
  }
  .brand-name {
    font-size: 32px; color: var(--brand-blue); letter-spacing: 0.5px;
  }
  .contact-band {
    position: absolute; left: 372px; top: 34px;
    width: 288px; height: 104px;
    background: var(--brand-blue);
    padding: 14px 0 0 16px;
    color: var(--paper); font-size: 11.5px; line-height: 21px;
  }
  .contact-line { display: flex; align-items: center; gap: 8px; }
  .contact-line svg { width: 11px; height: 11px; fill: var(--paper); flex: none; }
  .letter-body {
    position: absolute; left: 96px; top: 222px; width: 478px;
    font-size: 11.6px; line-height: 19px; color: var(--ink);
  }
  .letter-body p { margin-bottom: 19px; }
  .signature {
    position: absolute; left: 470px; top: 636px;
    color: var(--ink);
  }
  .signature-name { font-size: 16px; }
  .signature-title { font-size: 10px; color: var(--muted); margin-top: 4px; }
  .watermark {
    position: absolute; left: 40px; top: 650px;
    width: 250px; height: 250px; border-radius: 50%;
    border: 26px solid var(--watermark);
  }
  .footer-address {
    position: absolute; right: 84px; top: 752px;
    font-family: "Arimo", sans-serif; font-weight: 700;
    font-size: 12px; color: var(--brand-blue);
  }
  .footer-rule {
    position: absolute; left: 70px; right: 62px; top: 772px;
    height: 1.5px; background: var(--brand-blue);
  }
</style>
</head>
<body>
<main class="letterhead">
  <div class="contact-band">
    <div class="contact-line">
      <svg viewBox="0 0 24 24"><path d="M6.6 10.8a15 15 0 0 0 6.6 6.6l2.2-2.2c.3-.3.7-.4 1-.2 1.1.4 2.3.6 3.6.6.6 0 1 .4 1 1V20c0 .6-.4 1-1 1A17 17 0 0 1 3 4c0-.6.4-1 1-1h3.5c.6 0 1 .4 1 1 0 1.3.2 2.5.6 3.6.1.3 0 .7-.2 1z"/></svg>
      <span>555 014-2200</span>
    </div>
    <div class="contact-line">
      <svg viewBox="0 0 24 24"><path d="M7 1h10a2 2 0 0 1 2 2v18a2 2 0 0 1-2 2H7a2 2 0 0 1-2-2V3a2 2 0 0 1 2-2zm0 3v15h10V4z"/></svg>
      <span>555 014 3388</span>
    </div>
    <div class="contact-line">
      <svg viewBox="0 0 24 24"><path d="M2 5h20v14H2zm2 2v.5l8 5 8-5V7z"/></svg>
      <span>emarlow@brightvalehq.example</span>
    </div>
    <div class="contact-line">
      <svg viewBox="0 0 24 24"><path d="M12 2a10 10 0 1 0 0 20 10 10 0 0 0 0-20zm0 2c.9 1.2 1.6 2.6 2 4h-4c.4-1.4 1.1-2.8 2-4zM4.3 14a8 8 0 0 1 0-4h3.4a16 16 0 0 0 0 4zm.9 2h3c.3 1.3.8 2.5 1.5 3.6A8 8 0 0 1 5.2 16zm3-8h-3a8 8 0 0 1 4.5-3.6C9 5.5 8.5 6.7 8.2 8zM12 20c-.9-1.2-1.6-2.6-2-4h4c-.4 1.4-1.1 2.8-2 4zm2.3-6H9.7a14 14 0 0 1 0-4h4.6a14 14 0 0 1 0 4zm.3 5.6c.7-1.1 1.2-2.3 1.5-3.6h3a8 8 0 0 1-4.5 3.6zM16.3 14a16 16 0 0 0 0-4h3.4a8 8 0 0 1 0 4z"/></svg>
      <span>www.brightvalehq.example</span>
    </div>
  </div>

  <div class="corner-block"></div>
  <div class="brand">
    <div class="brand-dot"></div>
    <div class="brand-name">Brightvale HQ</div>
  </div>

  <div class="watermark" role="img" aria-label="Faint large circle decoration"></div>

  <section class="letter-body">
    <p>Lorem ipsum dolor sit amet, consectetur adipiscing elit. Donec orci purus, luctus vitae dignissim eu, iaculis sed purus. Vivamus faucibus, ipsum nec aliquet viverra, leo mauris condimentum ligula, sit amet sagittis enim ligula quis arcu. Nam egestas tortor id nisi porttitor mattis. In tortor ante, ultricies in suscipit a, tempus non massa. Vivamus et auctor mi. Fusce vel massa nulla. Phasellus nec eros mauris, et scelerisque orci. Donec malesuada orci vitae nulla accumsan porta a id massa.</p>
    <p>Quisque accumsan iaculis magna sit amet fringilla. Maecenas consequat, magna eget tincidunt semper, odio nibh rutrum mi, id feugiat ante nisi eu risus. Vestibulum nunc orci, rhoncus a placerat in, ultricies in mi. Cras mattis varius eros, vel fringilla nisi suscipit eget. Quisque scelerisque sagittis nulla at porttitor. Mauris a justo et tellus interdum tristique. Sed id augue vitae urna euismod commodo aliquet a quam. Pellentesque arcu velit, cursus et malesuada ut, consequat et diam. Nullam erat sem, rhoncus id ullamcorper vitae, rhoncus et arcu. In ultricies ultricies nulla.</p>
    <p>Kut rutrum nisi iaculis at. Donec eu magna a metus ornare faucibus. Fusce aliquet faucibus ultricies. Morbi semper, est id tincidunt gravida, sem arcu adipiscing lacus, ac bibendum nulla leo eu purus. Quisque nec diam sed risus consectetur a accumsan quis quis nibh. Vestibulum id purus lorem. Donec eu magna a metus ornare faucibus. Fusce aliquet faucibus ultricies. Morbi semper, est id tincidunt gravida, sem arcu adipiscing lacus, ac bibendum nulla leo eu purus. Quisque nec diam sed risus consectetur a accumsan quis quis nibh. Vestibulum id purus lorem.</p>
  </section>

  <div class="signature">
    <div class="signature-name">Evan Marlow</div>
    <div class="signature-title">Co-Founder &amp; CEO</div>
  </div>

  <div class="footer-address">742 Lakeside Avenue, Suite C-7 , Brightvale, ST 00000</div>
  <div class="footer-rule"></div>
</main>
</body>
</html>
```